Business Card Design Project

The overall design must be suitable alongside our company logo which is attached

There must be space for the agent to write their name & telephone number

Card must contain the words:

Brightwell Carpet Cleaning

Agent:
Tel:

Target Market(s)

qweqwe

Industry/Entity Type

Business

```html
<!DOCTYPE html>
<html lang="en">
<head>
<meta charset="utf-8">
<title>Brightwell Carpet Cleaning – Agent Card</title>
<link rel="stylesheet" href="https://fonts.googleapis.com/css2?family=Open+Sans:wght@400;600&display=swap">
<style>
  :root {
    --page-bg: #ece9e4;
    --card-bg: #ffffff;
    --ink: #2b2624;
    --ink-soft: #3a3a3a;
    --rule-dark: #4a4340;
    --rule-light: #b9b4b0;
    --dash: #c9c9c9;
  }
  html, body {
    margin: 0;
    width: 1200px;
    height: 1000px;
    overflow: hidden;
    background: var(--page-bg);
  }
  .business-card {
    position: absolute;
    left: 150px;
    top: 243px;
    width: 900px;
    height: 514px;
    background: var(--card-bg);
    box-shadow: 0 2px 10px rgba(0,0,0,0.12);
    font-family: "Open Sans", Arial, sans-serif;
    color: var(--ink-soft);
  }
  .field-label {
    position: absolute;
    font-size: 30px;
    font-weight: 600;
    letter-spacing: 2px;
  }
  .field-label--agent { left: 160px; top: 90px; }
  .field-label--tel { left: 160px; top: 172px; }
  .write-line {
    position: absolute;
    border-top: 2px dashed var(--dash);
    height: 0;
  }
  .write-line--agent { left: 300px; right: 110px; top: 124px; }
  .write-line--tel { left: 300px; right: 110px; top: 232px; }
  .base-rule {
    position: absolute;
    left: 0;
    right: 0;
    top: 0;
    height: 100%;
  }
  .brand {
    position: absolute;
    left: 60px;
    top: 330px;
    display: flex;
    align-items: center;
    gap: 18px;
  }
  .brand-mark {
    width: 70px;
    height: 70px;
    border-radius: 50%;
    background: var(--ink);
    flex: none;
  }
  .brand-name {
    font-family: "Open Sans", Arial, sans-serif;
    font-size: 36px;
    font-weight: 600;
    color: var(--ink);
    line-height: 1.1;
    width: 300px;
  }
</style>
</head>
<body>
  <section class="business-card">
    <span class="field-label field-label--agent">Agent:</span>
    <span class="write-line write-line--agent"></span>
    <span class="field-label field-label--tel">Tel:</span>
    <span class="write-line write-line--tel"></span>

    <svg class="base-rule" viewBox="0 0 900 514" preserveAspectRatio="none" aria-hidden="true">
      <line x1="190" y1="434" x2="900" y2="434" stroke="var(--rule-dark)" stroke-width="5"/>
      <line x1="190" y1="442" x2="900" y2="442" stroke="var(--rule-light)" stroke-width="2"/>
    </svg>

    <div class="brand">
      <span class="brand-mark"></span>
      <span class="brand-name">Brightwell Carpet Cleaning</span>
    </div>
  </section>
</body>
</html>
```